New Software Development Firm Needs Business Cards!

We just completed a successful logo design project on MakerHive and need to develop a business card design using that shiny new logo. We want a clean, modern design that communicates professionalism and tech savvy without being cliche'.

The company is "Bramble Logic, LLC", but our dba is "Bramble" The business card address should reflect the full company name in the address. The logo just uses "Bramble".

Photoshop or Illustrator source files will be required, along with exact font name(s) and source(s) used.

The design will need to work well with our letterhead as well. I'm also launching a project right now for letterhead and envelopes as well. Please submit to both projects! We're excited to see the designs. Thanks...

Target Market(s)

Small to medium business professionals

Industry/Entity Type

Business

Requirements
Must have
• Need place for:
- Company name and address (5 lines)
- Phone: (1 number)
- Fax: (1 number)
- Employee's name
- Employee's position
- Employee's email address
- Company web site URL
Nice to have
• Probably want a white card, but we're open to options.

```html
<!DOCTYPE html>
<html lang="en">
<head>
<meta charset="utf-8">
<title>Bramble Business Card</title>
<link href="https://fonts.googleapis.com/css2?family=Exo+2:wght@400&family=Ubuntu:wght@400;500;700&display=swap" rel="stylesheet">
<style>
  :root {
    --page: #e4e4e4;
    --card-black: #111111;
    --card-black-hi: #2a2a2a;
    --card-white: #ffffff;
    --card-white-lo: #e9e9e9;
    --accent-red: #e8141e;
    --ink: #1a1a1a;
    --logo-white: #ffffff;
  }
  * { box-sizing: border-box; margin: 0; padding: 0; }
  html, body { width: 1200px; height: 861px; overflow: hidden; }
  body {
    background: var(--page);
    position: relative;
    font-family: "Ubuntu", sans-serif;
  }
  .card {
    position: absolute;
    top: 258px;
    width: 540px;
    height: 340px;
    overflow: hidden;
    box-shadow: 0 6px 18px rgba(0,0,0,0.25);
  }
  .card-front { left: 40px; }
  .card-back { left: 620px; background: linear-gradient(180deg, var(--card-white) 40%, var(--card-white-lo) 100%); }

  .dark-texture {
    position: absolute;
    inset: 0;
    background: linear-gradient(160deg, var(--card-black-hi) 0%, var(--card-black) 60%, #050505 100%);
  }
  .card-back .dark-texture { bottom: auto; height: 128px; }

  .wordmark {
    position: absolute;
    left: 0; right: 0;
    text-align: center;
    font-family: "Exo 2", sans-serif;
    font-weight: 400;
    color: var(--logo-white);
    letter-spacing: 1px;
    line-height: 1;
  }
  .card-front .wordmark { top: 136px; font-size: 66px; }
  .card-back .wordmark { top: 32px; font-size: 62px; }

  .red-band {
    position: absolute;
    left: 0; top: 128px;
    width: 540px; height: 14px;
  }

  .contact-list {
    position: absolute;
    left: 36px; top: 154px;
    list-style: none;
    color: var(--ink);
    font-size: 15px;
    line-height: 18px;
  }
  .contact-list li { display: flex; align-items: flex-start; margin-bottom: 3px; }
  .contact-list .icon { width: 18px; height: 18px; flex: none; margin-right: 6px; }
  .contact-list .address-item { margin-bottom: 5px; }

  .person {
    position: absolute;
    right: 22px; top: 200px;
    text-align: right;
  }
  .person-name { color: var(--accent-red); font-weight: 500; font-size: 26px; line-height: 30px; }
  .person-position { color: var(--ink); font-weight: 500; font-size: 17px; line-height: 22px; }
</style>
</head>
<body>

<section class="card card-front">
  <div class="dark-texture" role="img" aria-label="Dark faceted triangle texture"></div>
  <div class="wordmark">Bramble</div>
</section>

<section class="card card-back">
  <div class="dark-texture" role="img" aria-label="Dark faceted triangle texture"></div>
  <div class="wordmark">Bramble</div>
  <svg class="red-band" viewBox="0 0 540 14" preserveAspectRatio="none">
    <rect width="540" height="14" fill="var(--accent-red)"/>
  </svg>

  <ul class="contact-list">
    <li class="address-item">
      <svg class="icon" viewBox="0 0 20 20"><circle cx="10" cy="10" r="8.5" fill="none" stroke="var(--accent-red)" stroke-width="2"/><path d="M10 4.5a3.5 3.5 0 0 0-3.5 3.5c0 2.6 3.5 6.5 3.5 6.5s3.5-3.9 3.5-6.5A3.5 3.5 0 0 0 10 4.5z" fill="var(--accent-red)"/><circle cx="10" cy="8" r="1.3" fill="#fff"/></svg>
      <span>Bramble Logic, LLC<br>88 Larkin Court, Suite 310<br>Brookfield, Oregon 97415<br>USA</span>
    </li>
    <li>
      <svg class="icon" viewBox="0 0 20 20"><circle cx="10" cy="10" r="8.5" fill="none" stroke="var(--accent-red)" stroke-width="2"/><path d="M6.5 5.5l2 .3.8 2.2-1.2.9c.6 1.3 1.6 2.3 2.9 2.9l.9-1.2 2.2.8.3 2-1.3 1c-3.6-.4-6.7-3.5-7.1-7.1z" fill="var(--accent-red)"/></svg>
      <span>(555) 214-7730</span>
    </li>
    <li>
      <svg class="icon" viewBox="0 0 20 20"><circle cx="10" cy="10" r="8.5" fill="none" stroke="var(--accent-red)" stroke-width="2"/><rect x="7" y="5" width="6" height="3.5" fill="var(--accent-red)"/><rect x="5" y="8.5" width="10" height="4.5" rx="1" fill="var(--accent-red)"/><rect x="7" y="12" width="6" height="3" fill="#fff" stroke="var(--accent-red)" stroke-width="1"/></svg>
      <span>(555) 214-7731</span>
    </li>
    <li>
      <svg class="icon" viewBox="0 0 20 20"><circle cx="10" cy="10" r="8.5" fill="none" stroke="var(--accent-red)" stroke-width="2"/><rect x="5" y="6.5" width="10" height="7" fill="var(--accent-red)"/><path d="M5 6.5l5 4 5-4" fill="none" stroke="#fff" stroke-width="1"/></svg>
      <span>name@bramblelogic.com</span>
    </li>
    <li>
      <svg class="icon" viewBox="0 0 20 20"><circle cx="10" cy="10" r="8.5" fill="none" stroke="var(--accent-red)" stroke-width="2"/><rect x="5" y="6.5" width="10" height="7" fill="var(--accent-red)"/><path d="M5 6.5l5 4 5-4" fill="none" stroke="#fff" stroke-width="1"/></svg>
      <span>www.bramblelogic.com</span>
    </li>
  </ul>

  <div class="person">
    <div class="person-name">Name Surname</div>
    <div class="person-position">Position</div>
  </div>
</section>

</body>
</html>
```